Calvanta Group Real Estate Company business cards

New business card design, we are generally happy with the basic layout of the existing front of business card, (feel free to change) but require a head shot photo on the back side.

http://www.calvanta.com.au/

Attached logos, and existing business card

------------------------------

Target Market(s)

Real estate

Industry/Entity Type

Real Estate

Contact Information for Business Card

Standard size double sided

Font styles to use
Other font styles liked:
• Futura

Requirements
Must have
• Photo head shot on the back side
Nice to have
• yes
Should not have
• No

```html
<!DOCTYPE html>
<html lang="en">
<head>
<meta charset="utf-8">
<title>Calvanta Group business cards</title>
<link href="https://fonts.googleapis.com/css2?family=Jost:wght@400;500;600&display=swap" rel="stylesheet">
<style>
  :root {
    --bg: #e9e8ee;
    --purple: #3b2482;
    --purple-deep: #2d1a6a;
    --purple-light: #4a3296;
    --orange: #f7941d;
    --white: #ffffff;
    --grey: #8d8aa6;
    --photo-tone: #c9c7cf;
  }
  * { box-sizing: border-box; margin: 0; padding: 0; }
  html, body { width: 1200px; height: 900px; overflow: hidden; }
  body {
    background: var(--bg);
    font-family: "Jost", "Futura", sans-serif;
    position: relative;
  }
  .card {
    position: absolute;
    width: 680px;
    height: 388px;
    border-radius: 4px;
    background: linear-gradient(135deg, var(--purple-light) 0%, var(--purple) 45%, var(--purple-deep) 100%);
    box-shadow: 0 14px 30px rgba(30, 20, 60, 0.28);
    color: var(--white);
    overflow: hidden;
  }
  /* Back side */
  .card--back { left: 80px; top: 56px; }
  .card--back .brand {
    position: absolute;
    left: 150px;
    top: 140px;
    font-size: 58px;
    font-weight: 500;
    letter-spacing: 1px;
    line-height: 1;
    color: var(--white);
  }
  .card--back .services {
    position: absolute;
    left: 156px;
    top: 218px;
    font-size: 24px;
    font-weight: 400;
    display: flex;
    align-items: center;
    gap: 16px;
  }
  .services .dot {
    width: 7px; height: 7px; border-radius: 50%;
    background: var(--orange);
  }
  .headshot {
    position: absolute;
    right: 36px;
    top: 28px;
    width: 124px;
    height: 96px;
    border: 3px solid var(--orange);
    background: linear-gradient(180deg, #e6e5ea 0%, var(--photo-tone) 60%, #3b3f55 100%);
  }
  /* Front side */
  .card--front { left: 440px; top: 456px; }
  .card--front .brand {
    position: absolute;
    left: 56px;
    top: 52px;
    font-size: 84px;
    font-weight: 500;
    letter-spacing: 1px;
    line-height: 1;
    color: var(--white);
  }
  .holder {
    position: absolute;
    left: 214px;
    top: 176px;
    display: flex;
    align-items: center;
    gap: 14px;
  }
  .holder .name { font-size: 22px; font-weight: 600; }
  .holder .role { font-size: 19px; font-weight: 400; }
  .holder .dot { width: 6px; height: 6px; border-radius: 50%; background: var(--orange); }
  .contacts {
    position: absolute;
    left: 72px;
    top: 222px;
    display: grid;
    grid-template-columns: auto auto;
    column-gap: 32px;
    row-gap: 14px;
    font-size: 19px;
    font-weight: 400;
  }
  .contact { display: flex; align-items: center; gap: 8px; white-space: nowrap; }
  .contact svg { width: 16px; height: 16px; flex: none; }
  .contact .label { color: var(--orange); font-weight: 500; }
</style>
</head>
<body>

  <section class="card card--back" aria-label="Business card back">
    <div class="headshot" role="img" aria-label="Head shot photo of the director"></div>
    <div class="brand">Calvanta Group</div>
    <div class="services">
      <span>Buy</span><span class="dot"></span>
      <span>Sell</span><span class="dot"></span>
      <span>Rent</span>
    </div>
  </section>

  <section class="card card--front" aria-label="Business card front">
    <div class="brand">Calvanta Group</div>
    <div class="holder">
      <span class="name">Daniel Tran</span>
      <span class="dot"></span>
      <span class="role">Director</span>
    </div>
    <div class="contacts">
      <div class="contact">
        <svg viewBox="0 0 16 16" aria-hidden="true"><path d="M4 1.5l2 3-1.3 1.3a8 8 0 0 0 5.5 5.5L11.5 10l3 2-1 2.5c-6 .3-12-5.7-12-12z" fill="none" stroke="var(--orange)" stroke-width="1.6" stroke-linejoin="round"/></svg>
        <span>0400 555 218</span>
      </div>
      <div class="contact">
        <svg viewBox="0 0 16 16" aria-hidden="true"><rect x="4" y="1.5" width="8" height="13" rx="1.5" fill="none" stroke="var(--orange)" stroke-width="1.6"/><circle cx="8" cy="12" r="0.9" fill="var(--orange)"/></svg>
        <span>daniel.tran@calvanta.com.au</span>
      </div>
      <div class="contact">
        <svg viewBox="0 0 16 16" aria-hidden="true"><circle cx="8" cy="8" r="6.5" fill="none" stroke="var(--orange)" stroke-width="1.4"/><ellipse cx="8" cy="8" rx="2.8" ry="6.5" fill="none" stroke="var(--orange)" stroke-width="1.2"/><path d="M1.5 8h13M2.5 4.8h11M2.5 11.2h11" stroke="var(--orange)" stroke-width="1.1"/></svg>
        <span>www.calvanta.com.au</span>
      </div>
      <div class="contact">
        <span class="label">ABN:</span>
        <span>41 208 365 917</span>
      </div>
    </div>
  </section>

</body>
</html>
```